Report Design

I am looking for a redesign of our monthly inspection reports we submit to our customers. I uploaded the current one we use (Tallowfern) and also that of a competitor (Cedar Knoll). I want to more copy the layout of the Cedarknoll report I attached but with more flow and design.

Requirements
Must have
• This has to be in a template format that we can modify the content every month.

```html
<!DOCTYPE html>
<html lang="en">
<head>
<meta charset="utf-8">
<title>Landscape Inspection Report Template</title>
<link rel="stylesheet" href="https://fonts.googleapis.com/css2?family=Oswald:wght@600;700&family=Lato:wght@400;700&family=Montserrat:wght@500&display=swap">
<style>
  :root {
    --stage: #8e8e8e;
    --paper: #ffffff;
    --green-bright: #22b232;
    --green-deep: #066a33;
    --green-title: #0e7a33;
    --green-frame: #3fcf3f;
    --label-green: #0b6b30;
    --ink: #222222;
    --muted: #9a9a9a;
    --black: #0b0b0b;
  }
  * { box-sizing: border-box; margin: 0; padding: 0; }
  html, body { width: 1200px; height: 2447px; overflow: hidden; }
  body { background: var(--stage); position: relative; font-family: 'Lato', sans-serif; }

  .sheet {
    position: absolute; width: 517px; height: 670px;
    background: var(--paper); overflow: hidden;
    box-shadow: 0 4px 14px rgba(0,0,0,0.28);
  }

  /* Cover */
  .cover { left: 315px; top: 136px; }
  .cover-shapes { position: absolute; inset: 0; width: 517px; height: 670px; }
  .cover-title {
    position: absolute; right: 44px; top: 42px; text-align: right;
    font-family: 'Oswald', sans-serif; font-weight: 700; font-size: 31px;
    line-height: 34px; color: var(--green-title); letter-spacing: -0.3px;
  }
  .cover-photo {
    position: absolute; left: 54px; top: 139px; width: 419px; height: 353px;
    border: 2px solid var(--green-frame);
    background: linear-gradient(180deg, #3f7a2c 0%, #2f6a23 45%, #d05a5a 72%, #58a032 80%, #6fbf3a 100%);
  }
  .cover-brand {
    position: absolute; left: 44px; top: 574px;
    display: flex; align-items: center; gap: 7px;
    font-family: 'Lato', sans-serif; font-weight: 700; font-size: 24px; color: var(--black);
  }
  .cover-brand .mark { width: 14px; height: 14px; border-radius: 50%; background: var(--green-bright); }
  .cover-contact {
    position: absolute; right: 47px; top: 538px; text-align: right;
    color: #fff; font-size: 8.5px; line-height: 11px;
  }
  .cover-contact .division { font-weight: 700; margin-bottom: 4px; }
  .cover-contact .row { display: flex; justify-content: flex-end; align-items: center; gap: 6px; }
  .cover-contact .row + .row { margin-top: 3px; }
  .cover-contact svg { width: 7px; height: 7px; flex: none; }

  /* Report pages */
  .page-header {
    position: absolute; left: 0; top: 0; width: 100%; height: 111px;
    background: linear-gradient(90deg, var(--green-bright) 0%, #16962f 55%, var(--green-deep) 100%);
  }
  .page-title {
    position: absolute; left: 0; top: 34px; width: 100%; text-align: center;
    font-family: 'Oswald', sans-serif; font-weight: 700; font-size: 31px;
    line-height: 40px; color: #fff; letter-spacing: -0.2px;
  }
  .month-pill {
    position: absolute; left: 84px; top: 90px; width: 334px; height: 40px;
    border-radius: 20px; background: var(--black); color: #fff;
    font-family: 'Montserrat', sans-serif; font-weight: 500; font-size: 20px;
    display: flex; align-items: center; justify-content: center;
  }
  .photo {
    position: absolute; left: 54px; width: 201px; height: 163px;
    border: 2px solid var(--green-frame); border-radius: 9px;
  }
  .photo.top { top: 176px; }
  .photo.bottom { top: 407px; }
  .inset {
    position: absolute; left: 28px; width: 105px; height: 72px;
    border: 2px solid var(--green-frame); border-radius: 6px; z-index: 2;
  }
  .inset.top { top: 145px; }
  .inset.low { top: 521px; height: 84px; }
  .item-label {
    position: absolute; left: 59px; width: 191px; height: 22px; border-radius: 11px;
    background: var(--label-green); color: #fff; font-weight: 700; font-size: 12.5px;
    display: flex; align-items: center; justify-content: center;
  }
  .item-label.top { top: 351px; }
  .item-label.bottom { top: 579px; }
  .item-label.low { top: 617px; }
  .item-note {
    position: absolute; left: 277px; width: 205px;
    font-size: 11.3px; line-height: 14.2px; color: var(--ink);
  }
  .item-note.top { top: 199px; }
  .item-note.bottom { top: 441px; }
  .page-number { position: absolute; right: 34px; top: 629px; font-size: 7px; color: var(--muted); }

  .p1 { left: 56px; top: 870px; }
  .p2 { left: 605px; top: 870px; }
  .p3 { left: 56px; top: 1600px; }
  .p4 { left: 605px; top: 1600px; }

  /* Photo placeholder tones */
  .tone-grass { background: linear-gradient(180deg, #cfd6da 0%, #a9b59a 40%, #b7789a 62%, #6c8a45 100%); }
  .tone-wall { background: linear-gradient(90deg, #d9d4c9 0%, #c9c3b6 60%, #7f8a63 100%); }
  .tone-street { background: linear-gradient(180deg, #9aa2a8 0%, #8a8f92 45%, #b9bcbc 60%, #5f7a3a 100%); }
  .tone-palm { background: linear-gradient(180deg, #c7ced3 0%, #5d7a44 45%, #4e6b38 70%, #8b8e8f 100%); }
  .tone-bed { background: linear-gradient(180deg, #c2cbd0 0%, #6f8a4d 40%, #4b6a33 70%, #5b4f3f 100%); }
  .tone-shrub { background: linear-gradient(180deg, #b9c3c7 0%, #8f9994 35%, #47692f 65%, #3d5b2a 100%); }
  .tone-mulch { background: linear-gradient(180deg, #d8d2c6 0%, #c3bdb0 40%, #8a8d8f 60%, #8b7c63 100%); }
  .tone-small-palm { background: linear-gradient(180deg, #d9d5cc 0%, #6d8747 45%, #4a6332 60%, #8f9293 100%); }
  .tone-copper { background: linear-gradient(180deg, #b8c2c6 0%, #d5d3cc 35%, #9a2a36 60%, #6d2030 100%); }
</style>
</head>
<body>

<section class="sheet cover">
  <svg class="cover-shapes" viewBox="0 0 544 704" preserveAspectRatio="none" aria-hidden="true">
    <defs>
      <linearGradient id="coverGreen" x1="0" y1="0" x2="1" y2="1">
        <stop offset="0" stop-color="#22b232"/>
        <stop offset="1" stop-color="#087034"/>
      </linearGradient>
    </defs>
    <polygon points="0,0 100,0 300,220 300,388 57,388 0,325" fill="url(#coverGreen)"/>
    <polygon points="544,432 544,704 360,704 190,520 190,400 498,381" fill="url(#coverGreen)"/>
  </svg>
  <h1 class="cover-title">LANDSCAPE, IRR. &amp;<br>PROPERTY INSPECTION</h1>
  <div class="cover-photo" role="img" aria-label="Photo of a landscaped front yard with porch, shrubs, red flower bed and lawn"></div>
  <div class="cover-brand"><span class="mark"></span>Tallowfern</div>
  <div class="cover-contact">
    <div class="division">Landscape and Grounds Maintenance<br>Division</div>
    <div class="row"><span>4410 Orchard Bend Road<br>Fernvale, FL 33000</span>
      <svg viewBox="0 0 10 10"><path d="M5 0a3.5 3.5 0 0 0-3.5 3.5C1.5 6 5 10 5 10s3.5-4 3.5-6.5A3.5 3.5 0 0 0 5 0zm0 5a1.5 1.5 0 1 1 0-3 1.5 1.5 0 0 1 0 3z" fill="#4cd44c"/></svg></div>
    <div class="row"><span>555-210-4837</span>
      <svg viewBox="0 0 10 10"><path d="M2 0l2 2.5-1 1.2c.6 1.3 1.6 2.3 2.9 2.9l1.2-1L10 8l-1.5 2C4 10 0 6 0 1.5z" fill="#4cd44c"/></svg></div>
    <div class="row"><span>555-318-9021</span>
      <svg viewBox="0 0 10 10"><rect x="0.5" y="3" width="9" height="6" rx="1" fill="none" stroke="#4cd44c"/><rect x="2.5" y="1" width="5" height="3" fill="#4cd44c"/></svg></div>
  </div>
</section>

<section class="sheet p1">
  <header class="page-header"><h2 class="page-title">GARDENS ON HARLOW POA &amp; RETAIL</h2></header>
  <div class="month-pill">MONTH OF NOVEMBER</div>
  <div class="inset top tone-wall" role="img" aria-label="Photo of ornamental grasses along a building wall"></div>
  <div class="photo top tone-grass" role="img" aria-label="Photo of blooming pink Muhly grass in a bed"></div>
  <div class="item-label top">1. Grasses Throughout:</div>
  <p class="item-note top">Right now the Muhly grass is blooming and looks great. The crew went around and trimmed them all up so they look fresh and clean. There were some of the types that were not blooming, that we trimmed back farther.</p>
  <div class="photo bottom tone-street" role="img" aria-label="Photo of an entrance island bed beside a crosswalk"></div>
  <div class="item-label bottom">2. Flowers:</div>
  <p class="item-note bottom">Both main entrances are in need of fresh flowers.</p>
  <span class="page-number">Page 1</span>
</section>

<section class="sheet p2">
  <header class="page-header"><h2 class="page-title">GARDENS ON HARLOW POA &amp; RETAIL</h2></header>
  <div class="month-pill">MONTH OF NOVEMBER</div>
  <div class="inset top tone-palm" role="img" aria-label="Photo of tall palms along an entrance road"></div>
  <div class="photo top tone-palm" role="img" aria-label="Photo of palms with dead fronds near a parking lot"></div>
  <div class="item-label top">3. Palms Need Trimming:</div>
  <p class="item-note top">All the Palms could use a trimming, there are dead frons and some hanging seed pods and boots. Let us know if and when you would like to get this scheduled.</p>
  <div class="photo bottom tone-bed" role="img" aria-label="Photo of a corner shrub bed damaged by trucks"></div>
  <div class="item-label bottom">4. Fill In:</div>
  <p class="item-note bottom">We should fill this corner in where truck run over the corner with additional plants.</p>
  <span class="page-number">Page 2</span>
</section>

<section class="sheet p3">
  <header class="page-header"><h2 class="page-title">GARDENS ON HARLOW POA...CONT</h2></header>
  <div class="month-pill">MONTH OF NOVEMBER</div>
  <div class="inset top tone-shrub" role="img" aria-label="Photo of a thin coontie bed beside a building"></div>
  <div class="photo top tone-shrub" role="img" aria-label="Photo of a parking island with coonties and a young tree"></div>
  <div class="item-label top">5. Fill in Coonties:</div>
  <p class="item-note top">Coonties need to be filled in here. As well as side of Burger Barn.</p>
  <div class="photo bottom tone-mulch" role="img" aria-label="Photo of a washed out bed along a building curb"></div>
  <div class="item-label bottom">6. Mulch:</div>
  <p class="item-note bottom">Overall the place could use fresh mulch, or we could just mulch these washed out areas that are an eye sore.</p>
  <span class="page-number">Page 3</span>
</section>

<section class="sheet p4">
  <header class="page-header"><h2 class="page-title">GARDENS ON HARLOW POA...CONT</h2></header>
  <div class="month-pill">MONTH OF NOVEMBER</div>
  <div class="photo top tone-small-palm" role="img" aria-label="Photo of small pruned palms along a building walkway"></div>
  <div class="item-label top">7. Pruning:</div>
  <p class="item-note top">All the little palms have been pruned up to look clean</p>
  <div class="photo bottom tone-copper" role="img" aria-label="Photo of red copper plants lining a sidewalk"></div>
  <div class="inset low tone-copper" role="img" aria-label="Photo of copper plants at a curb corner"></div>
  <div class="item-label low">8. Plants filling in:</div>
  <p class="item-note bottom">The copper plants and Jasmine are all filling in nicely</p>
  <span class="page-number">Page 4</span>
</section>

</body>
</html>
```